Post card for annual skin cancer screening exam

We are looking to design a modern, classy, clean, but fun postcard that we will send out to patients to remind them to schedule their follow up exams for our dermatology office.

It should include our logo
http://tovimek.com/design/logo/jpg/tovimek2.jpg
http://tovimek.com/design/logo/jpg/tovimek.jpg

Address
Phone number
website

We are open to your ideas on wording, as something clever is always appreciated - though this is going to both young and elderly patients - so the message must be easy to read and clear.
Updates

Font styles to use
Serif

Colors
85cae6
3176b5

Requirements
Must have
• Logo
• Office address
• Phone number
• website
• call to action message - to schedule a follow up visit

```html
<!DOCTYPE html>
<html lang="en">
<head>
<meta charset="utf-8">
<title>Tovimek Dermatology – Skin Exam Reminder Postcard</title>
<link rel="stylesheet" href="https://fonts.googleapis.com/css2?family=Arimo:ital,wght@0,400;0,700;1,700&family=Tinos&display=swap">
<style>
  :root {
    --navy: #1a4f86;
    --brand-blue: #3176b5;
    --bright-blue: #0f78c0;
    --sky-light: #85cae6;
    --sky-mid: #4f95d6;
    --band: #1c5d98;
    --white: #ffffff;
    --paper: #f1f1f1;
    --line: #444a52;
    --teal: #1b9bcf;
  }
  * { box-sizing: border-box; margin: 0; padding: 0; }
  html, body {
    width: 753px; height: 1200px; overflow: hidden;
    background: var(--paper);
  }
  .stage {
    position: relative;
    width: 722px; height: 1149px;
    transform: scale(1.0429);
    transform-origin: 0 0;
  }
  .card {
    position: absolute;
    left: 28px;
    width: 667px; height: 515px;
    overflow: hidden;
    box-shadow: 0 2px 8px rgba(0,0,0,.28);
  }
  .card--front { top: 30px; height: 513px; }
  .card--back { top: 605px; background: var(--white); }
  .card svg.art { position: absolute; inset: 0; }

  /* front */
  .brand {
    position: absolute;
    display: flex; align-items: center; gap: 10px;
    font-family: "Arimo", sans-serif;
    font-weight: 400;
  }
  .brand__dot {
    width: 30px; height: 30px; border-radius: 50%;
  }
  .brand--front { left: 392px; top: 88px; color: var(--white); font-size: 25px; }
  .brand--front .brand__dot { border: 2px solid var(--white); }
  .brand--back { left: 392px; top: 432px; color: var(--teal); font-size: 25px; }
  .brand--back .brand__dot { border: 2px solid var(--teal); }

  .message {
    position: absolute;
    left: 259px; top: 270px;
    font-family: "Arimo", sans-serif;
    font-style: italic; font-weight: 700;
    color: var(--white);
    text-shadow: 1px 2px 3px rgba(0,0,0,.35);
  }
  .message__lead { font-size: 21px; letter-spacing: .3px; }
  .message__ask { font-size: 28.5px; line-height: 37px; margin-top: 20px; letter-spacing: .2px; }

  .call-band {
    position: absolute;
    left: 0; right: 0; bottom: 0; height: 58px;
    display: flex; align-items: center; justify-content: center;
    font-family: "Arimo", sans-serif;
    font-style: italic; font-weight: 700;
    font-size: 19.5px; letter-spacing: 1.4px;
    color: var(--white);
  }

  /* back */
  .pill {
    position: absolute; left: 0;
    height: 29px;
    background: var(--white);
    border-radius: 0 14px 14px 0;
    padding-left: 27px;
    display: flex; align-items: center;
    font-family: "Arimo", sans-serif; font-weight: 700;
    font-size: 16px; letter-spacing: .6px;
    color: var(--teal);
  }
  .pill--reminder { top: 72px; width: 237px; }
  .pill--contact { top: 335px; width: 134px; }

  .fields { position: absolute; left: 27px; top: 144px; }
  .field {
    display: flex; align-items: flex-end;
    height: 39px;
    font-family: "Tinos", serif; font-size: 17px;
    color: var(--white);
  }
  .field__blank { border-bottom: 1px solid var(--white); margin-left: 3px; height: 17px; }
  .field__unit { font-size: 14px; margin-left: 8px; }

  .contact { position: absolute; left: 27px; top: 382px; list-style: none; }
  .contact li {
    display: flex; align-items: flex-start; gap: 7px;
    font-family: "Arimo", sans-serif; color: var(--white);
    font-size: 16px; letter-spacing: .4px;
    margin-bottom: 12px;
  }
  .contact li.contact__address { font-size: 13px; line-height: 16px; letter-spacing: .6px; }
  .contact svg { flex: none; margin-top: 1px; }

  .stamp-box {
    position: absolute; left: 539px; top: 57px;
    width: 83px; height: 111px;
    border: 1px solid var(--line);
  }
  .address-lines { position: absolute; left: 368px; top: 234px; width: 255px; }
  .address-lines span { display: block; height: 1px; background: var(--line); margin-bottom: 34px; }
</style>
</head>
<body>
<main class="stage">

  <section class="card card--front" aria-label="Postcard front">
    <svg class="art" width="667" height="513" viewBox="0 0 667 513">
      <defs>
        <linearGradient id="header-fill" x1="0" y1="0" x2="1" y2="0.4">
          <stop offset="0" stop-color="#0c80c6"/>
          <stop offset="1" stop-color="#1a4f86"/>
        </linearGradient>
        <linearGradient id="sky-fill" x1="0" y1="0" x2="1" y2="1">
          <stop offset="0" stop-color="#3b57b8"/>
          <stop offset=".45" stop-color="#3f8fd6"/>
          <stop offset="1" stop-color="#cfe6f5"/>
        </linearGradient>
        <linearGradient id="band-fill" x1="0" y1="0" x2="1" y2="0">
          <stop offset="0" stop-color="#1b7fc4"/>
          <stop offset="1" stop-color="#1c5390"/>
        </linearGradient>
      </defs>
      <rect width="667" height="513" fill="url(#header-fill)"/>
      <path role="img" aria-label="Photo of a white daisy against a bright blue sky with soft clouds"
            d="M0 62 C150 88 260 208 400 205 C520 202 590 158 667 154 V455 H0 Z" fill="url(#sky-fill)"/>
      <path d="M8 67 C150 90 260 210 400 206 C520 202 590 158 665 155" fill="none" stroke="#ffffff" stroke-width="3.5"/>
      <rect y="455" width="667" height="58" fill="url(#band-fill)"/>
    </svg>

    <div class="brand brand--front"><span class="brand__dot"></span>Tovimek Dermatology</div>

    <div class="message">
      <p class="message__lead">Just A friendly reminder.....</p>
      <p class="message__ask">Please call to schedule<br>your full body skin exam</p>
    </div>

    <p class="call-band">Call us today : (555) 014-2290</p>
  </section>

  <section class="card card--back" aria-label="Postcard back">
    <svg class="art" width="667" height="515" viewBox="0 0 667 515">
      <defs>
        <linearGradient id="panel-fill" x1="0" y1="0" x2="1" y2="1">
          <stop offset="0" stop-color="#1f8ccc"/>
          <stop offset="1" stop-color="#1a5a97"/>
        </linearGradient>
      </defs>
      <path d="M0 0 H302 C340 40 332 130 292 232 C256 330 268 460 332 515 H0 Z" fill="url(#panel-fill)"/>
    </svg>

    <p class="pill pill--reminder">Appointment Reminder</p>

    <div class="fields">
      <p class="field">For:<span class="field__blank" style="width:207px"></span></p>
      <p class="field">Place:<span class="field__blank" style="width:195px"></span></p>
      <p class="field">Date:<span class="field__blank" style="width:195px"></span></p>
      <p class="field">Time:<span class="field__blank" style="width:57px"></span><span class="field__unit">AM/PM</span></p>
    </div>

    <p class="pill pill--contact">Contact Us</p>

    <ul class="contact">
      <li>
        <svg width="17" height="17" viewBox="0 0 17 17" aria-hidden="true">
          <circle cx="8.5" cy="8.5" r="7.5" fill="none" stroke="#fff" stroke-width="1.3"/>
          <path d="M5.6 4.6l1.4-.3 1 2-.9.8c.4 1 1.1 1.7 2.1 2.1l.8-.9 2 1-.3 1.4c-3 .3-6.4-3.1-6.1-6.1z" fill="#fff"/>
        </svg>
        (555) 014-2290
      </li>
      <li>
        <svg width="17" height="17" viewBox="0 0 17 17" aria-hidden="true" fill="none" stroke="#fff" stroke-width="1.2">
          <circle cx="8.5" cy="8.5" r="7.5"/>
          <ellipse cx="8.5" cy="8.5" rx="3.2" ry="7.5"/>
          <path d="M1 8.5h15M2.3 4.8h12.4M2.3 12.2h12.4"/>
        </svg>
        www.tovimek.com
      </li>
      <li class="contact__address">
        <svg width="17" height="19" viewBox="0 0 17 19" aria-hidden="true">
          <path d="M8.5 1a5.5 5.5 0 0 0-5.5 5.5c0 4 5.5 11 5.5 11s5.5-7 5.5-11A5.5 5.5 0 0 0 8.5 1z" fill="#fff"/>
          <circle cx="8.5" cy="6.5" r="2" fill="#1c6aa8"/>
        </svg>
        <span>214 Maple Grove Avenue<br>Fairview NY 10990</span>
      </li>
    </ul>

    <div class="stamp-box" aria-label="Stamp area"></div>
    <div class="address-lines" aria-label="Mailing address lines"><span></span><span></span><span></span><span></span></div>

    <div class="brand brand--back"><span class="brand__dot"></span>Tovimek Dermatology</div>
  </section>

</main>
</body>
</html>
```